Experienced Home remodel service

I'm a home remodeler. I want a catch phrase that clearly describes viewers what kind of work I'm in like the purple phrase on my rough draft idea. I need my website, phone, logo, slogan included. The picture is of my daughter. I want her on it. Be cool if something could be added to her picture like a hard hat or tool belt ect and her picture cut out/background removed. Some kind of background other than plain white for whole picture. I added extra pics of her so pick one

Target Market(s)

Home owners between 30-60

Industry/Entity Type

Home renovation/remodel

Colors

Designer to choose colors to be used in the design.

Requirements
Must have
• Daughters picture incorporated. Logo, phone, website address, slogan,
Nice to have
• See a hardhat or tool belt added to one of my daughters pictures that is chosen to use by designer

```html
<!DOCTYPE html>
<html lang="en">
<head>
<meta charset="utf-8">
<title>Harlow Home Solutions</title>
<link href="https://fonts.googleapis.com/css2?family=Krona+One&family=Questrial&display=swap" rel="stylesheet">
<style>
  :root {
    --teal-deep: #053f4d;
    --teal: #14a1aa;
    --lime: #b9c93e;
    --sun: #f1d21f;
    --orange: #d9670f;
    --band-brown: #56342c;
    --footer: #232123;
    --white: #ffffff;
    --yellow: #ffff00;
  }
  html, body {
    margin: 0;
    padding: 0;
    width: 1200px;
    height: 763px;
    overflow: hidden;
    background: #ffffff;
  }
  .sign {
    position: relative;
    width: 1200px;
    height: 763px;
    overflow: hidden;
    background: linear-gradient(100deg, var(--teal-deep) 0%, #0a6470 22%, var(--teal) 40%, var(--lime) 58%, var(--sun) 74%, var(--orange) 100%);
    font-family: "Krona One", sans-serif;
    color: var(--white);
  }
  .footer-bar {
    position: absolute;
    left: 0;
    top: 680px;
    width: 1200px;
    height: 83px;
    background: var(--footer);
  }
  .photo-hero {
    position: absolute;
    left: 683px;
    top: 50px;
    width: 482px;
    height: 630px;
    background: linear-gradient(180deg, #f4d535 0%, #e6c7a8 30%, #e4c9ec 55%, #d9b8e4 100%);
    clip-path: polygon(145px 0, 340px 0, 345px 120px, 420px 280px, 482px 480px, 470px 630px, 70px 630px, 40px 470px, 30px 400px, 80px 300px, 100px 160px, 140px 110px);
  }
  .photo-thumb {
    position: absolute;
    left: 42px;
    top: 572px;
    width: 228px;
    height: 191px;
    background: linear-gradient(180deg, #d9b38a 0%, #e2b9a0 45%, #3a3436 100%);
    clip-path: polygon(60px 0, 140px 0, 165px 55px, 180px 60px, 190px 105px, 228px 140px, 228px 191px, 0 191px, 20px 140px, 55px 100px);
  }
  .brand-mark {
    position: absolute;
    left: 72px;
    top: 92px;
    width: 104px;
    height: 104px;
    background: var(--white);
  }
  .brand-name {
    position: absolute;
    margin: 0;
    font-family: "Krona One", sans-serif;
    font-weight: 400;
    color: var(--white);
    line-height: 1;
    white-space: nowrap;
  }
  .brand-name--main { left: 218px; top: 118px; font-size: 100px; }
  .brand-name--sub { left: 90px; top: 222px; font-size: 50px; letter-spacing: 5px; }
  .services-band {
    position: absolute;
    left: 70px;
    top: 302px;
    width: 700px;
    height: 139px;
    background: var(--band-brown);
  }
  .services-text {
    position: absolute;
    margin: 0;
    font-size: 56px;
    line-height: 1;
    white-space: nowrap;
  }
  .services-text--top { left: 90px; top: 312px; }
  .services-text--bottom { left: 192px; top: 375px; }
  .tagline {
    position: absolute;
    left: 90px;
    top: 448px;
    margin: 0;
    font-family: "Questrial", sans-serif;
    font-size: 48px;
    line-height: 52px;
    color: var(--yellow);
    font-weight: 700;
    letter-spacing: 3px;
  }
  .phone {
    position: absolute;
    left: 226px;
    top: 592px;
    font-size: 56px;
    line-height: 1;
    white-space: nowrap;
  }
  .website {
    position: absolute;
    left: 292px;
    top: 696px;
    font-family: "Questrial", sans-serif;
    font-weight: 700;
    font-size: 40px;
    letter-spacing: 8.4px;
    line-height: 1;
    white-space: nowrap;
  }
</style>
</head>
<body>
  <main class="sign">
    <div class="footer-bar"></div>
    <div class="photo-hero" role="img" aria-label="Cut-out photo of the owner's smiling daughter in a yellow hard hat and lilac puffer jacket, holding a hammer"></div>
    <div class="photo-thumb" role="img" aria-label="Cut-out photo of the owner's daughter giving a thumbs up"></div>

    <div class="brand-mark"></div>
    <h1 class="brand-name brand-name--main">HARLOW</h1>
    <p class="brand-name brand-name--sub">HOME SOLUTIONS</p>

    <div class="services-band"></div>
    <p class="services-text services-text--top">BUILD~REPAIR</p>
    <p class="services-text services-text--bottom">REPLACE</p>

    <p class="tagline">FOR ALL YOUR HOME<br>REMODEL NEEDS</p>

    <div class="phone">555-214-6083</div>

    <div class="website">www.harlowhomesolutions.com</div>
  </main>
</body>
</html>
```